Simple graphic for a book or slide presentation

We are looking for a style that suits the style of our book. It's title is Harbor. Keeping a calm course through stormy seas. There will be more line drawing/graphics in the book but how you design this image will create the style for all the other simple graphics in the book (once we decide what they are). So this one design will lead to a few more to match the style of this one. We'd like the shape of the overall graphic (i.e the arrows and words/bubbles) to be circular (not a rounded square as appears in the sample attached). Perhaps the words don't need to be in ovals or bound by anything at all; perhaps they do - let's see what you see. We'd like you to choose a font or offer many different fonts you think will capture the practical yet unconventional tone of the book. The book is teaching that managing risks in life is a life-skill that can be learned. The section of the book where this graphic will be placed is called "the power of language" - basically we are saying that thoughts, words and actions create our culture and our destiny. This insight comes from Torvel Pelloru's famous quote:
Carefully watch your thoughts, for they become your words.
Manage and watch your words, for they will become your actions.
Consider and judge your actions, for they have become your habits.
Acknowledge and watch your habits, for they shall become your values.
Understand and embrace your values, for they become your destiny.

Please change the text in the middle of the graphic to say: The Human Culture Cycle

```html
<!DOCTYPE html>
<html lang="en">
<head>
<meta charset="utf-8">
<title>The Human Culture Cycle</title>
<link rel="stylesheet" href="https://fonts.googleapis.com/css2?family=Roboto+Condensed:wght@700&family=Ubuntu:wght@400;700&display=swap">
<style>
  :root {
    --page: #e9e9eb;
    --board: #ffffff;
    --culture: #fd8c4e;
    --thoughts: #74b959;
    --words-soft: #f5d960;
    --words: #fcc200;
    --actions: #e42b61;
    --habits: #474665;
    --values: #1fb8ea;
    --ink: #333333;
    --accent: #f2b705;
    --ring: #b5bac0;
  }
  * { margin: 0; padding: 0; box-sizing: border-box; }
  html, body { width: 1200px; height: 593px; overflow: hidden; background: var(--page); }
  .canvas { position: relative; width: 1200px; height: 593px; }
  .board {
    position: absolute; top: 42px; width: 553px; height: 525px;
    background: var(--board);
    box-shadow: 0 3px 8px rgba(0,0,0,.18);
  }
  .board--labels { left: 24px; }
  .board--quotes { left: 623px; }
  .board svg { display: block; width: 100%; height: 100%; }
  .seg-culture { fill: var(--culture); }
  .seg-thoughts { fill: var(--thoughts); }
  .seg-words-soft { fill: var(--words-soft); }
  .seg-words { fill: var(--words); }
  .seg-actions { fill: var(--actions); }
  .seg-habits { fill: var(--habits); }
  .seg-values { fill: var(--values); }
  .label { font-family: "Ubuntu", sans-serif; font-weight: 700; fill: #fff; }
  .label--big { font-size: 44px; text-anchor: middle; }
  .label--small { font-size: 34px; }
  .desc { font-family: "Ubuntu", sans-serif; font-weight: 400; font-size: 20px; fill: #fff; }
  .title { font-family: "Roboto Condensed", sans-serif; font-weight: 700; font-size: 58px; fill: var(--ink); text-anchor: middle; }
  .title-rule { stroke: var(--accent); stroke-width: 6; stroke-linecap: round; }
  .cycle-line { fill: none; stroke: var(--ring); stroke-width: 3; }
  .cycle-node { fill: #fff; stroke: var(--ring); stroke-width: 3; }
  .hub-ring { fill: none; stroke: #d9dce0; stroke-width: 3; }
</style>
</head>
<body>
<div class="canvas">

  <svg width="0" height="0" style="position:absolute" aria-hidden="true">
    <defs>
      <filter id="soft-shadow" x="-10%" y="-10%" width="120%" height="120%">
        <feDropShadow dx="0" dy="2" stdDeviation="6" flood-color="#000" flood-opacity=".16"/>
      </filter>
      <g id="cycle-frame">
        <circle class="cycle-line" cx="596" cy="565" r="492"/>
        <g transform="translate(596 565)">
          <path class="cycle-line" d="M0 -492 m-14 -10 l16 10 l-16 10"/>
          <path class="cycle-line" d="M0 -492 m-14 -10 l16 10 l-16 10" transform="rotate(60)"/>
          <path class="cycle-line" d="M0 -492 m-14 -10 l16 10 l-16 10" transform="rotate(120)"/>
          <path class="cycle-line" d="M0 -492 m-14 -10 l16 10 l-16 10" transform="rotate(180)"/>
          <path class="cycle-line" d="M0 -492 m-14 -10 l16 10 l-16 10" transform="rotate(240)"/>
          <path class="cycle-line" d="M0 -492 m-14 -10 l16 10 l-16 10" transform="rotate(300)"/>
          <circle class="cycle-node" cx="-246" cy="-426" r="9"/>
          <circle class="cycle-node" cx="246" cy="-426" r="9"/>
          <circle class="cycle-node" cx="492" cy="0" r="9"/>
          <circle class="cycle-node" cx="246" cy="426" r="9"/>
          <circle class="cycle-node" cx="-246" cy="426" r="9"/>
          <circle class="cycle-node" cx="-492" cy="0" r="9"/>
        </g>
        <circle cx="596" cy="565" r="446" fill="#fff" filter="url(#soft-shadow)"/>
      </g>
      <g id="hub">
        <circle cx="596" cy="565" r="196" fill="#fff" filter="url(#soft-shadow)"/>
        <circle class="hub-ring" cx="596" cy="565" r="178"/>
        <line class="title-rule" x1="566" y1="478" x2="626" y2="478"/>
        <text class="title" x="598" y="572">The Human</text>
        <text class="title" x="596" y="642">Culture Cycle</text>
        <line class="title-rule" x1="566" y1="682" x2="626" y2="682"/>
      </g>
    </defs>
  </svg>

  <div class="board board--labels">
    <svg viewBox="0 0 1186 1125" aria-label="The Human Culture Cycle, headings">
      <use href="#cycle-frame"/>
      <path class="seg-thoughts" d="M596 565 L596 135 A430 430 0 0 1 982.5 376.5 Z"/>
      <path class="seg-words-soft" d="M596 565 L982.5 376.5 A430 430 0 0 1 982.5 753.5 Z"/>
      <path class="seg-actions" d="M596 565 L982.5 753.5 A430 430 0 0 1 596 995 Z"/>
      <path class="seg-habits" d="M596 565 L596 995 A430 430 0 0 1 209.5 753.5 Z"/>
      <path class="seg-values" d="M596 565 L209.5 753.5 A430 430 0 0 1 209.5 376.5 Z"/>
      <path class="seg-culture" d="M596 565 L209.5 376.5 A430 430 0 0 1 596 135 Z"/>
      <use href="#hub"/>
      <text class="label label--big" x="433" y="313">CULTURE</text>
      <text class="label label--big" x="753" y="313">THOUGHTS</text>
      <text class="label label--big" x="912" y="581">WORDS</text>
      <text class="label label--big" x="280" y="581">VALUES</text>
      <text class="label label--big" x="437" y="855">HABITS</text>
      <text class="label label--big" x="773" y="855">ACTIONS</text>
    </svg>
  </div>

  <div class="board board--quotes">
    <svg viewBox="0 0 1186 1125" aria-label="The Human Culture Cycle, with quote">
      <use href="#cycle-frame"/>
      <path class="seg-thoughts" d="M596 565 L596 135 A430 430 0 0 1 982.5 376.5 Z"/>
      <path class="seg-words" d="M596 565 L982.5 376.5 A430 430 0 0 1 982.5 753.5 Z"/>
      <path class="seg-actions" d="M596 565 L982.5 753.5 A430 430 0 0 1 596 995 Z"/>
      <path class="seg-habits" d="M596 565 L596 995 A430 430 0 0 1 209.5 753.5 Z"/>
      <path class="seg-values" d="M596 565 L209.5 753.5 A430 430 0 0 1 209.5 376.5 Z"/>
      <path class="seg-culture" d="M596 565 L209.5 376.5 A430 430 0 0 1 596 135 Z"/>
      <use href="#hub"/>

      <text class="label label--small" x="554" y="253" text-anchor="end">CULTURE</text>
      <text class="desc" text-anchor="end">
        <tspan x="554" y="294">Creats a supportive</tspan>
        <tspan x="554" y="321">culture and society</tspan>
      </text>

      <text class="label label--small" x="634" y="253">THOUGHTS</text>
      <text class="desc">
        <tspan x="642" y="294">Carefully watch your</tspan>
        <tspan x="642" y="321">thoughts, for they become</tspan>
        <tspan x="642" y="348">your words.</tspan>
      </text>

      <text class="label label--small" x="992" y="509" text-anchor="end">WORDS</text>
      <text class="desc" text-anchor="end">
        <tspan x="994" y="554">Manage and watch</tspan>
        <tspan x="994" y="581">your words, for they</tspan>
        <tspan x="994" y="608">will become your</tspan>
        <tspan x="994" y="635">actions.</tspan>
      </text>

      <text class="label label--small" x="212" y="504">VALUES</text>
      <text class="desc">
        <tspan x="212" y="549">Understand and</tspan>
        <tspan x="212" y="576">embrace your</tspan>
        <tspan x="212" y="603">values, for they</tspan>
        <tspan x="212" y="630">become your</tspan>
        <tspan x="212" y="657">destiny.</tspan>
      </text>

      <text class="label label--small" x="437" y="797" text-anchor="middle">HABITS</text>
      <text class="desc" text-anchor="middle">
        <tspan x="437" y="836">Acknowledge and watch</tspan>
        <tspan x="437" y="863">your habits, for they shall</tspan>
        <tspan x="437" y="890">become your values.</tspan>
      </text>

      <text class="label label--small" x="764" y="797" text-anchor="middle">ACTIONS</text>
      <text class="desc" text-anchor="middle">
        <tspan x="764" y="836">Consider and judge your</tspan>
        <tspan x="764" y="863">actions, for they have</tspan>
        <tspan x="764" y="890">become your habits.</tspan>
      </text>
    </svg>
  </div>

</div>
</body>
</html>
```